Modernise Business Card

Our company has been operating for 10 years. With the start of the new decade we are looking to refresh our business card design. We manufacture a range of industrial product shipping to customers internationally. A copy of our current card, both sides, is attached. We are looking for a mature professional appearance.

```html
<!DOCTYPE html>
<html lang="en">
<head>
<meta charset="utf-8">
<title>Korvex Business Card</title>
<link href="https://fonts.googleapis.com/css2?family=Saira:ital,wght@0,400;0,500;0,700;1,700&display=swap" rel="stylesheet">
<style>
  :root {
    --backdrop: #1a1a1c;
    --card: #262729;
    --card-accent: #263a43;
    --brand-blue: #1fa9e1;
    --ink-light: #eef1f3;
    --rule: #cfd3d6;
  }
  * { box-sizing: border-box; margin: 0; padding: 0; }
  html, body { width: 1200px; height: 900px; overflow: hidden; }
  body {
    background: var(--backdrop);
    font-family: "Saira", sans-serif;
    color: var(--ink-light);
    position: relative;
  }
  .card {
    position: absolute;
    left: 290px;
    width: 620px;
    height: 355px;
    background: var(--card);
    box-shadow: 0 14px 30px rgba(0,0,0,.55);
    overflow: hidden;
  }
  .card--front { top: 62px; }
  .card--back { top: 478px; }

  .front-accent { position: absolute; inset: 0; }

  .product-list {
    position: absolute;
    right: 318px;
    top: 92px;
    text-align: right;
    font-size: 19px;
    line-height: 25px;
    letter-spacing: 1.5px;
    text-transform: uppercase;
  }

  .wordmark {
    position: absolute;
    display: flex;
    align-items: center;
    gap: 16px;
  }
  .wordmark__square {
    width: 22px;
    height: 22px;
    border: 2px solid var(--ink-light);
  }
  .wordmark__name {
    font-weight: 500;
    color: var(--brand-blue);
    font-size: 48px;
    letter-spacing: 5px;
    line-height: 1;
  }
  .card--front .wordmark { right: 48px; top: 148px; }
  .card--back .wordmark { left: 46px; top: 58px; }

  .holder-name {
    position: absolute;
    left: 46px;
    top: 150px;
    font-size: 30px;
    font-weight: 700;
    color: var(--brand-blue);
  }
  .divider {
    position: absolute;
    left: 46px;
    right: 40px;
    top: 196px;
    border-top: 1px solid var(--rule);
  }
  .contact-list {
    position: absolute;
    left: 46px;
    top: 210px;
    list-style: none;
    font-size: 17px;
    line-height: 25px;
  }
  .contact-list li { display: flex; align-items: center; gap: 8px; }
  .contact-list svg { width: 16px; height: 16px; flex: none; }
  .contact-list .label { color: var(--brand-blue); }

  .address {
    position: absolute;
    right: 40px;
    bottom: 30px;
    text-align: right;
    font-size: 17px;
    line-height: 25px;
    font-style: normal;
  }
</style>
</head>
<body>

<section class="card card--front">
  <svg class="front-accent" viewBox="0 0 620 355" preserveAspectRatio="none" aria-hidden="true">
    <polygon points="0,0 120,0 330,355 0,355" fill="var(--card-accent)"/>
  </svg>
  <p class="product-list">Hydraulic Adapters<br>Hose Fittings<br>Quick Couplings</p>
  <div class="wordmark">
    <span class="wordmark__square"></span>
    <span class="wordmark__name">KORVEX</span>
  </div>
</section>

<section class="card card--back">
  <div class="wordmark">
    <span class="wordmark__square"></span>
    <span class="wordmark__name">KORVEX</span>
  </div>
  <h1 class="holder-name">Alan Pryce</h1>
  <hr class="divider">
  <ul class="contact-list">
    <li>
      <svg viewBox="0 0 16 16" aria-hidden="true"><circle cx="8" cy="8" r="6.5" fill="none" stroke="var(--brand-blue)" stroke-width="1.4"/><path d="M5.6 5c.6 2.6 2.3 4.6 5 5.6l.8-1.2-1.4-.8-.7.6c-1-.5-1.8-1.3-2.3-2.3l.6-.7-.8-1.4z" fill="var(--brand-blue)"/></svg>
      <span><span class="label">Ch:</span> +86 139 5520 4471</span>
    </li>
    <li>
      <svg viewBox="0 0 16 16" aria-hidden="true"><circle cx="8" cy="8" r="6.5" fill="none" stroke="var(--brand-blue)" stroke-width="1.4"/><path d="M5.6 5c.6 2.6 2.3 4.6 5 5.6l.8-1.2-1.4-.8-.7.6c-1-.5-1.8-1.3-2.3-2.3l.6-.7-.8-1.4z" fill="var(--brand-blue)"/></svg>
      <span><span class="label">Au:</span> +61 412 738 915</span>
    </li>
    <li>
      <svg viewBox="0 0 16 16" aria-hidden="true"><rect x="1.5" y="3.5" width="13" height="9" fill="none" stroke="var(--brand-blue)" stroke-width="1.4"/><path d="M1.5 3.5 8 9l6.5-5.5" fill="none" stroke="var(--brand-blue)" stroke-width="1.4"/></svg>
      <span>apryce@korvexfittings.com</span>
    </li>
    <li>
      <svg viewBox="0 0 16 16" aria-hidden="true"><circle cx="8" cy="8" r="6.5" fill="none" stroke="var(--brand-blue)" stroke-width="1.4"/><ellipse cx="8" cy="8" rx="2.8" ry="6.5" fill="none" stroke="var(--brand-blue)" stroke-width="1.2"/><path d="M1.5 8h13M2.5 5h11M2.5 11h11" stroke="var(--brand-blue)" stroke-width="1.1"/></svg>
      <span>www.korvexfittings.com</span>
    </li>
  </ul>
  <address class="address">
    907-3, Lian Feng Building<br>
    412 Qiaoxin Road, Haishu District<br>
    Hangzhou 310000 China
  </address>
</section>

</body>
</html>
```